Kelvard Engineers: Why you should hire us keepsake

New design. Open to plastic cards. We are an engineering firm that designs cell phone towers and commercial buildings. Please check out our website www.kelvardeng.example for more details. We want people to remember our card and for it to be useful if possible. We want the same look and feel on these cards to be translated to other marketing material we may need such as brochures.

Target Market(s)

Architects, Developers and Telecommunication Carriers

Industry/Entity Type

Engineering

Contact Information for Business Card

Card with our company colors, logo, and innovative design with elements related to our industry.

Font styles to use
Sans Serif

Colors
9bcb3c
abd036
0255a3

Requirements
Must have
• Sleek and hip design
Nice to have
• Bright lime green and navy coloring that pops with an innovative design.
Should not have
• A basic and boring design

```html
<!DOCTYPE html>
<html lang="en">
<head>
<meta charset="utf-8">
<title>Kelvard Engineers – Business Card</title>
<link href="https://fonts.googleapis.com/css2?family=Roboto:wght@400;500;700;900&display=swap" rel="stylesheet">
<style>
  :root {
    --lime: #d3d62a;
    --lime-deep: #abd036;
    --navy: #1f3566;
    --navy-light: #2c4a86;
    --white: #ffffff;
    --ink: #1f3566;
    --backdrop: #2b2b2b;
  }
  * { margin: 0; padding: 0; box-sizing: border-box; }
  html, body { width: 1200px; height: 930px; overflow: hidden; }
  body {
    background: var(--backdrop);
    font-family: "Roboto", Arial, sans-serif;
    position: relative;
  }
  .card {
    position: absolute;
    width: 540px;
    height: 310px;
    border-radius: 18px;
    overflow: hidden;
  }
  /* Front */
  .card-front {
    left: 90px; top: 110px;
    background: var(--lime);
  }
  .card-front .wordmark {
    position: absolute;
    left: 0; right: 0; top: 92px;
    text-align: center;
    font-size: 92px;
    font-weight: 900;
    color: var(--white);
    letter-spacing: -2px;
    line-height: 1;
  }
  .card-front .cities {
    position: absolute;
    left: 0; right: 0; bottom: 34px;
    text-align: center;
    font-size: 15px;
    font-weight: 500;
    color: var(--white);
    letter-spacing: 1.5px;
    text-transform: uppercase;
  }
  .cities .sep { margin: 0 8px; opacity: .85; }
  /* Back */
  .card-back {
    left: 570px; top: 500px;
    background: var(--navy);
  }
  .card-back .panel { position: absolute; inset: 0; }
  .card-back .brand {
    position: absolute;
    left: 34px; top: 96px;
  }
  .brand .wordmark {
    font-size: 64px;
    font-weight: 900;
    color: var(--lime);
    letter-spacing: -1.5px;
    line-height: 1;
  }
  .brand .tagline {
    margin-top: 10px;
    font-size: 12.5px;
    font-weight: 500;
    color: var(--white);
    letter-spacing: 1px;
    text-transform: uppercase;
    white-space: nowrap;
  }
  .card-back .contact {
    position: absolute;
    right: 26px; top: 44px;
    text-align: right;
    color: var(--ink);
  }
  .contact .name { font-size: 19px; font-weight: 500; }
  .contact .role { font-size: 13px; color: var(--lime); margin-bottom: 12px; }
  .contact .line {
    display: flex; justify-content: flex-end; align-items: center;
    gap: 8px;
    font-size: 13px;
    line-height: 20px;
    white-space: nowrap;
  }
  .contact .line svg { width: 11px; height: 11px; fill: none; stroke: var(--lime); stroke-width: 1.6; flex: none; }
  .card-back .edge-tab {
    position: absolute; right: 0; top: 42px;
    width: 6px; height: 30px;
    background: var(--navy);
    border-left: 3px solid var(--lime);
  }
</style>
</head>
<body>
  <section class="card card-front">
    <div class="wordmark">Kelvard</div>
    <p class="cities">Northvale<span class="sep">|</span>Eastbrook<span class="sep">|</span>Westford<span class="sep">|</span>Southmere Bay</p>
  </section>

  <section class="card card-back">
    <svg class="panel" viewBox="0 0 540 310" preserveAspectRatio="none" aria-hidden="true">
      <polygon points="0,0 355,0 215,310 0,310" fill="#1f3566"/>
      <polygon points="355,0 215,310 340,310 272,196" fill="#2c4a86" opacity=".55"/>
      <polygon points="360,0 540,0 540,232 272,196" fill="#ffffff"/>
    </svg>
    <div class="edge-tab"></div>
    <div class="brand">
      <div class="wordmark">Kelvard</div>
      <div class="tagline">Multi-Discipline Engineering</div>
    </div>
    <div class="contact">
      <div class="name">Dana Holloway Pryce</div>
      <div class="role">Director</div>
      <div class="line">555.014.2231
        <svg viewBox="0 0 12 12"><path d="M2 1.5 4 1.5 5 4 3.8 5a6 6 0 0 0 3.2 3.2L8 7l2.5 1v2A1 1 0 0 1 9.5 11 8.5 8.5 0 0 1 1 2.5 1 1 0 0 1 2 1.5Z"/></svg></div>
      <div class="line">555.017.6642
        <svg viewBox="0 0 12 12"><rect x="3" y="1" width="6" height="10" rx="1"/><path d="M5.5 9h1"/></svg></div>
      <div class="line">dpryce@kelvardeng.example
        <svg viewBox="0 0 12 12"><rect x="1" y="2.5" width="10" height="7"/><path d="M1 2.5 6 6.5 11 2.5"/></svg></div>
      <div class="line">www.kelvardeng.example
        <svg viewBox="0 0 12 12"><circle cx="6" cy="6" r="5"/><path d="M1 6h10M6 1c2.5 3 2.5 7 0 10M6 1c-2.5 3-2.5 7 0 10"/></svg></div>
    </div>
  </section>
</body>
</html>
```